Torvane Vision and Core Values

We are wanting to promote our core values and vision on posters at our office. I have uploaded a copy of our logo. We would like to incorporate that, the vision and the core values. ALL THREE MUST BE INCLUDED ON THE DESIGN. For reference, our website is www.torvane-petroworks.example

Our vision is:
We are a Team of Power and Strength that Builds our People and Serves our Industry and Communities.

Our Values are:
We Operate with a Standard of Excellence.
We Do the Right Thing Every Time.
We Value and Recognize our People.
We are Team Players.
We Think and Act with Optimism and Faith.

```html
<!DOCTYPE html>
<html lang="en">
<head>
<meta charset="utf-8">
<title>Torvane Vision and Core Values</title>
<link rel="stylesheet" href="https://fonts.googleapis.com/css2?family=Montserrat:wght@400;700;800&family=Poppins:wght@400;600;700&display=swap">
<style>
  :root {
    --stage: #eeeeee;
    --paper-light: #f6f9fb;
    --paper-tint: #d3e3ee;
    --brand-red: #d3381c;
    --brand-navy: #1f3a6e;
    --ink: #111111;
    --text-navy: #17263f;
    --value-blue: #1b7fc4;
    --value-navy: #1e3c6a;
    --value-slate: #5f7390;
    --value-cyan: #1b9fd8;
    --value-sky: #22acdc;
  }
  * { margin: 0; padding: 0; box-sizing: border-box; }
  html, body { width: 1200px; height: 2320px; overflow: hidden; background: var(--stage); }
  .canvas { position: relative; width: 1200px; height: 2320px; }
  .poster {
    position: absolute; left: 40px; top: 354px;
    width: 710px; height: 1022px;
    transform: scale(1.5775); transform-origin: 0 0;
    background:
      radial-gradient(ellipse 60% 45% at 72% 55%, rgba(255,255,255,0.95), rgba(255,255,255,0) 70%),
      linear-gradient(160deg, var(--paper-tint) 0%, var(--paper-light) 45%, #e4eef5 75%, #f2f6f9 100%);
    box-shadow: -14px 12px 24px rgba(0,0,0,0.18);
    overflow: hidden;
  }
  .brand { position: absolute; left: 362px; top: 28px; width: 240px; text-align: center; }
  .brand-mark { width: 46px; height: 46px; border-radius: 50%; background: var(--brand-red); margin: 0 auto 16px; }
  .brand-name { font-family: "Poppins", sans-serif; font-weight: 700; font-size: 38px; line-height: 1; color: var(--brand-navy); letter-spacing: 2px; }
  .headline { position: absolute; left: 0; top: 0; }
  .headline text { font-family: "Montserrat", sans-serif; font-weight: 700; fill: var(--brand-red); }
  .vision {
    position: absolute; left: 64px; top: 705px; width: 260px; height: 272px;
    border: 2px dashed #1a1a1a; border-radius: 4px;
  }
  .vision-title { position: absolute; left: 30px; top: 10px; font-family: "Poppins", sans-serif; font-weight: 700; font-size: 50px; line-height: 50px; color: var(--ink); }
  .vision-text { position: absolute; left: 38px; top: 126px; width: 168px; font-family: "Montserrat", sans-serif; font-weight: 400; font-size: 16px; line-height: 20.5px; color: #222; }
  .values { position: absolute; left: 359px; top: 0; width: 260px; }
  .value { position: absolute; left: 0; width: 258px; height: 118px; }
  .value svg { position: absolute; left: 0; top: 0; }
  .value-text { position: absolute; left: 100px; top: 27px; width: 132px; font-family: "Poppins", sans-serif; font-weight: 700; font-size: 15px; line-height: 18px; color: var(--text-navy); }
</style>
</head>
<body>
<div class="canvas">
  <div class="poster">
    <div class="brand">
      <div class="brand-mark"></div>
      <div class="brand-name">TORVANE</div>
    </div>

    <svg class="headline" width="300" height="700" viewBox="0 0 300 700" aria-label="Our Values">
      <text x="139" y="655" font-size="92" textLength="305" lengthAdjust="spacingAndGlyphs" transform="rotate(-90 139 655)">OUR</text>
      <text x="259" y="655" font-size="92" textLength="585" lengthAdjust="spacingAndGlyphs" transform="rotate(-90 259 655)">VALUES</text>
    </svg>

    <section class="vision">
      <h2 class="vision-title">Our<br>vision</h2>
      <p class="vision-text">We are a Team of Power and Strength that Builds our People and Serves our Industry and Communities.</p>
    </section>

    <section class="values">
      <div class="value" style="top:238px">
        <svg width="258" height="118" viewBox="0 0 258 118">
          <path d="M38 114 Q78 110 78 58 Q78 2 120 2 H238 Q254 2 254 18 V98 Q254 114 238 114 H165" fill="none" stroke="var(--value-blue)" stroke-width="2"/>
          <circle cx="36" cy="58" r="32" fill="#fff" opacity="0.9"/>
          <circle cx="36" cy="58" r="26" fill="var(--value-blue)"/>
          <g fill="none" stroke="#fff" stroke-width="1.6"><rect x="30" y="44" width="18" height="24" rx="2"/><path d="M34 52 H44 M34 57 H44 M34 62 H41"/><circle cx="27" cy="58" r="5"/></g>
        </svg>
        <p class="value-text">We Operate with a Standard of Excellence.</p>
      </div>
      <div class="value" style="top:382px">
        <svg width="258" height="118" viewBox="0 0 258 118">
          <path d="M38 114 Q78 110 78 58 Q78 2 120 2 H238 Q254 2 254 18 V98 Q254 114 238 114 H165" fill="none" stroke="var(--value-navy)" stroke-width="2"/>
          <circle cx="36" cy="58" r="32" fill="#fff" opacity="0.9"/>
          <circle cx="36" cy="58" r="26" fill="var(--value-navy)"/>
          <g fill="none" stroke="#fff" stroke-width="1.6"><path d="M36 44 L49 51 V66 L36 73 L23 66 V51 Z M23 51 L36 58 L49 51 M36 58 V73"/></g>
        </svg>
        <p class="value-text">We Do the Right Thing Every Time.</p>
      </div>
      <div class="value" style="top:525px">
        <svg width="258" height="118" viewBox="0 0 258 118">
          <path d="M38 114 Q78 110 78 58 Q78 2 120 2 H238 Q254 2 254 18 V98 Q254 114 238 114 H165" fill="none" stroke="var(--value-slate)" stroke-width="2"/>
          <circle cx="36" cy="58" r="32" fill="#fff" opacity="0.9"/>
          <circle cx="36" cy="58" r="26" fill="var(--value-slate)"/>
          <g fill="none" stroke="#fff" stroke-width="1.6"><circle cx="36" cy="56" r="11"/><circle cx="36" cy="56" r="5"/><path d="M32 68 V74 H40 V68"/></g>
        </svg>
        <p class="value-text">We Value and Recognize our People.</p>
      </div>
      <div class="value" style="top:672px">
        <svg width="258" height="118" viewBox="0 0 258 118">
          <path d="M38 114 Q78 110 78 58 Q78 2 120 2 H238 Q254 2 254 18 V98 Q254 114 238 114 H165" fill="none" stroke="var(--value-cyan)" stroke-width="2"/>
          <circle cx="36" cy="58" r="32" fill="#fff" opacity="0.9"/>
          <circle cx="36" cy="58" r="26" fill="var(--value-cyan)"/>
          <g fill="none" stroke="#fff" stroke-width="1.6"><circle cx="36" cy="48" r="4"/><circle cx="26" cy="54" r="3.5"/><circle cx="46" cy="54" r="3.5"/><path d="M30 70 V60 Q36 55 42 60 V70 M21 68 V62 Q24 59 28 61 M51 68 V62 Q48 59 44 61"/></g>
        </svg>
        <p class="value-text">We are Team Players.</p>
      </div>
      <div class="value" style="top:828px">
        <svg width="258" height="118" viewBox="0 0 258 118">
          <path d="M38 114 Q78 110 78 58 Q78 2 120 2 H238 Q254 2 254 18 V98 Q254 114 238 114 H165" fill="none" stroke="var(--value-sky)" stroke-width="2"/>
          <circle cx="36" cy="58" r="32" fill="#fff" opacity="0.9"/>
          <circle cx="36" cy="58" r="26" fill="var(--value-sky)"/>
          <g fill="none" stroke="#fff" stroke-width="1.6"><path d="M36 42 A9 9 0 0 1 41 58 V62 H31 V58 A9 9 0 0 1 36 42 Z M32 65 H40"/><path d="M22 66 Q28 66 32 70 H44 L50 64"/></g>
        </svg>
        <p class="value-text">We Think and Act with Optimism and Faith.</p>
      </div>
    </section>
  </div>
</div>
</body>
</html>
```